Business Card Design Project

We need a business card design for a consultancy called 'Amber Ridge'. The design should communicate innovation and professionalism. The colors used should complement our logo. Please include source files for winning design.
Updates

Industry/Entity Type

Business

Colors

Designer to choose colors to be used in the design.

Requirements
Must have
• Card size should be 85mm x 50mm. The back side of the card should be the logo on a black background. The front side should display the name 'Amber Ridge' along with standard information. The front's design should graphically complement the back.
Nice to have
• Any graphical elements in the front the complement the back side (with the logo on a black background) would be a plus.

```html
<!DOCTYPE html>
<html lang="en">
<head>
<meta charset="utf-8">
<title>Amber Ridge – Business Card</title>
<link href="https://fonts.googleapis.com/css2?family=Cinzel:wght@500&family=Arimo:wght@400;700&display=swap" rel="stylesheet">
<style>
  :root {
    --backdrop: #2b2b2b;
    --card-black: #0b0b0b;
    --card-white: #ffffff;
    --amber: #e9a94c;
    --orange: #f07a26;
    --gold-light: #f1d58c;
    --ink: #1c1c1c;
    --muted: #6a6a6a;
    --soft-grey: #e6e6e6;
  }
  * { margin: 0; padding: 0; box-sizing: border-box; }
  html, body { width: 1200px; height: 1000px; overflow: hidden; }
  body {
    background: var(--backdrop);
    font-family: "Arimo", Arial, sans-serif;
    position: relative;
  }
  .card {
    position: absolute;
    left: 260px;
    width: 680px;
    height: 400px;
    border-radius: 22px;
    overflow: hidden;
    box-shadow: 0 14px 30px rgba(0,0,0,0.45);
  }
  .card--front { top: 70px; }
  .card--back { top: 530px; background: var(--card-black); }
  .card__shapes { position: absolute; inset: 0; width: 100%; height: 100%; }

  .brand-name {
    font-family: "Cinzel", "Times New Roman", serif;
    font-weight: 500;
    color: var(--amber);
    letter-spacing: 1px;
    white-space: nowrap;
  }

  /* front */
  .front__web {
    position: absolute; left: 44px; top: 44px;
    font-size: 17px; color: var(--ink);
  }
  .front__title { position: absolute; left: 398px; top: 38px; font-size: 34px; }
  .front__address {
    position: absolute; left: 400px; top: 92px;
    font-size: 14px; line-height: 19px; color: var(--muted);
    white-space: nowrap;
  }
  .front__direct {
    position: absolute; left: 420px; top: 318px;
    font-size: 15px; line-height: 20px; color: var(--muted);
    white-space: nowrap;
  }
  .front__person { position: absolute; left: 40px; top: 298px; }
  .front__name {
    display: block; width: 250px;
    background: var(--soft-grey);
    padding: 6px 14px;
    font-weight: 700; font-size: 21px; color: var(--ink);
  }
  .front__role {
    display: block; padding: 4px 16px;
    font-size: 17px; color: var(--muted);
  }

  /* back */
  .back__mark {
    position: absolute; left: 430px; top: 70px;
    width: 150px; height: 150px; border-radius: 50%;
    background: var(--amber);
  }
  .back__title { position: absolute; left: 330px; top: 236px; font-size: 44px; }
  .back__web {
    position: absolute; left: 250px; top: 330px;
    font-size: 16px; color: var(--muted);
  }
</style>
</head>
<body>

<section class="card card--front" aria-label="Card front">
  <svg class="card__shapes" viewBox="0 0 680 400" preserveAspectRatio="none" aria-hidden="true">
    <defs>
      <linearGradient id="frontStripe" x1="0" y1="0" x2="0" y2="1">
        <stop offset="0" stop-color="#f1d58c"/>
        <stop offset="1" stop-color="#f07a26"/>
      </linearGradient>
    </defs>
    <rect width="680" height="400" fill="var(--card-white)"/>
    <path d="M250 0 Q330 170 360 400" fill="none" stroke="url(#frontStripe)" stroke-width="12"/>
    <path d="M258 0 Q338 170 368 400 L680 400 L680 0 Z" fill="var(--card-black)"/>
  </svg>
  <p class="front__web">www.amberridge-consult.com</p>
  <h1 class="front__title brand-name">Amber Ridge</h1>
  <p class="front__address">
    Head Office: 14 Harbour Lane,<br>
    Suite 210, Westfield Park<br>
    Tel: +44 (020) 555 01 42<br>
    Fax: +44 (020) 555 01 43
  </p>
  <p class="front__direct">
    lena.marsh@amberridge-consult.com<br>
    0770 5550 1234
  </p>
  <div class="front__person">
    <span class="front__name">LENA MARSH</span>
    <span class="front__role">Sales Manager</span>
  </div>
</section>

<section class="card card--back" aria-label="Card back">
  <svg class="card__shapes" viewBox="0 0 680 400" preserveAspectRatio="none" aria-hidden="true">
    <defs>
      <linearGradient id="backStripe" x1="1" y1="0" x2="0" y2="1">
        <stop offset="0" stop-color="#f1d58c"/>
        <stop offset="1" stop-color="#f07a26"/>
      </linearGradient>
      <linearGradient id="backBand" x1="0" y1="0" x2="1" y2="1">
        <stop offset="0" stop-color="#ffffff"/>
        <stop offset="1" stop-color="#cfcfcf"/>
      </linearGradient>
    </defs>
    <path d="M0 0 H310 Q110 60 0 215 Z" fill="url(#backBand)"/>
    <path d="M310 0 Q110 60 0 215" fill="none" stroke="url(#backStripe)" stroke-width="7"/>
  </svg>
  <span class="back__mark" aria-hidden="true"></span>
  <h2 class="back__title brand-name">Amber Ridge</h2>
  <p class="back__web">www.amberridge-consult.com</p>
</section>

</body>
</html>
```